TBR CONTRACTING

I am looking for a logo/design for my business. Would like some unique symbol, would also like it to be double sided. On the back perhaps 3 pictures of some work we have done. I will attach some photos.

I would also like the colours to be orange and black or a dark grey and Orange.

Only writing I would like to see are:

(Contact number) 416-382-7146
(Name) Lewis Pardoe
(Email) lpardoe@quillmail.ca

Industry/Entity Type

Business

```html
<!DOCTYPE html>
<html lang="en">
<head>
<meta charset="utf-8">
<title>TBR Contracting – Business Card</title>
<link href="https://fonts.googleapis.com/css2?family=Quicksand:wght@500;600;700&display=swap" rel="stylesheet">
<style>
  :root {
    --charcoal: #363435;
    --band: #e6e7e8;
    --ink-light: #ececec;
    --orange: #ee6f1f;
    --page: #ffffff;
  }
  * { margin: 0; padding: 0; box-sizing: border-box; }
  html, body { width: 1200px; height: 1005px; overflow: hidden; background: var(--page); }
  body { position: relative; font-family: "Quicksand", sans-serif; color: var(--ink-light); }

  .card { position: absolute; background: var(--charcoal); overflow: hidden; }
  .card--front { left: 255px; top: 53px; width: 726px; height: 425px; }
  .card--back  { left: 257px; top: 525px; width: 724px; height: 425px; }

  .band { position: absolute; left: 0; width: 100%; background: var(--band); }

  .wordmark {
    position: absolute; left: 0; width: 100%; text-align: center;
    font-weight: 700; color: var(--ink-light); white-space: nowrap;
  }
  .card--front .wordmark { top: 205px; font-size: 40px; letter-spacing: 2px; }
  .wordmark-dot {
    display: inline-block; width: 18px; height: 18px; background: var(--orange);
    margin-right: 14px; vertical-align: 3px;
  }

  .front-email {
    position: absolute; top: 362px; left: 0; width: 100%; text-align: center;
    font-size: 30px; font-weight: 600; color: var(--ink-light);
  }

  .gallery { position: absolute; top: 66px; left: 0; width: 100%; height: 157px; display: flex; gap: 1px; }
  .gallery-photo { height: 100%; }
  .gallery-photo--kitchen  { width: 241px; background: linear-gradient(135deg, #d9d6d0, #8a5a3a 60%, #4a3a34); }
  .gallery-photo--basement { width: 245px; background: linear-gradient(180deg, #c9c4ba 0%, #b7a99a 55%, #b5763e 70%, #9c5e2c); }
  .gallery-photo--playroom { width: 236px; background: linear-gradient(180deg, #dcd6cc 0%, #cfc6b8 60%, #bfae93); }

  .name-tab { position: absolute; left: 0; top: 272px; width: 141px; height: 39px; background: var(--band); }
  .name {
    position: absolute; left: 151px; top: 272px; font-size: 30px; font-weight: 600; line-height: 40px;
  }
  .contact { position: absolute; left: 21px; display: flex; align-items: center; gap: 6px; font-size: 20px; font-weight: 600; }
  .contact--phone { top: 337px; }
  .contact--email { top: 371px; }
  .contact svg { width: 21px; height: 21px; }

  .card--back .wordmark { left: 470px; width: 220px; top: 322px; font-size: 24px; letter-spacing: 1px; }
</style>
</head>
<body>

<section class="card card--front" aria-label="Card front">
  <div class="wordmark"><span class="wordmark-dot"></span>TBR CONTRACTING</div>
  <div class="band" style="top:340px;height:9px;"></div>
  <p class="front-email">lpardoe@quillmail.ca</p>
</section>

<section class="card card--back" aria-label="Card back">
  <div class="band" style="top:56px;height:10px;"></div>
  <div class="gallery">
    <div class="gallery-photo gallery-photo--kitchen" role="img" aria-label="Photo of a renovated kitchen with wood cabinets and a sunroom"></div>
    <div class="gallery-photo gallery-photo--basement" role="img" aria-label="Photo of a finished basement with hardwood floor and built-in shelving"></div>
    <div class="gallery-photo gallery-photo--playroom" role="img" aria-label="Photo of a finished basement playroom with small tables"></div>
  </div>
  <div class="band" style="top:223px;height:9px;"></div>

  <div class="name-tab"></div>
  <p class="name">Lewis Pardoe</p>

  <p class="contact contact--phone">
    <svg viewBox="0 0 22 22" fill="none" stroke="currentColor" stroke-width="1.5">
      <rect x="1" y="1" width="20" height="20" rx="4"/>
      <path d="M7 5.5c-1 .6-1.6 1.6-1.2 3 1 3.4 3.6 6.2 7 7.4 1.3.4 2.4-.1 3-1l-2.2-2-1.6 1c-1.6-.8-2.8-2-3.6-3.6l1-1.6z" fill="currentColor"/>
    </svg>
    416-382-7146
  </p>
  <p class="contact contact--email">
    <svg viewBox="0 0 22 22" fill="none" stroke="currentColor" stroke-width="1.3">
      <rect x="1" y="1" width="20" height="20" rx="4"/>
      <circle cx="11" cy="11" r="6"/>
      <ellipse cx="11" cy="11" rx="2.6" ry="6"/>
      <path d="M5 11h12M6 8h10M6 14h10"/>
    </svg>
    lpardoe@quillmail.ca
  </p>

  <div class="wordmark">TBR CONTRACTING</div>
</section>

</body>
</html>
```